Update New Business Card - For Start Up

I need to update my business card, I have our old version for example. I would like to keep to the same colors and theme. We are a threat reporting and case management tool for corporations and educational institutions.

Target Market(s)

Corporate Security and Human Resources, School Administrators and Superintendents.

Industry/Entity Type

Physical Security and Technology.

Contact Information for Business Card

My Name, Founder/CEO, phone number 555-214-6082, Logo, Web...

Colors
0054AA
0677BA
7BADD7
CADEEF
E8F1F8

Requirements
Must have
• Something new and trendy.

```html
<!DOCTYPE html>
<html lang="en">
<head>
<meta charset="utf-8">
<title>Vantorel Business Card</title>
<link rel="stylesheet" href="https://fonts.googleapis.com/css2?family=Montserrat:wght@400;600;700&display=swap">
<style>
  :root {
    --page: #ffffff;
    --front-base: #eeeeee;
    --front-tone: #dcddde;
    --brand-blue: #1f77c0;
    --back-base: #1e74bb;
    --back-tone: #2185d5;
    --ink: #4a4a4a;
    --ink-strong: #3c3c3c;
    --white: #ffffff;
  }
  * { box-sizing: border-box; margin: 0; padding: 0; }
  html, body { width: 982px; height: 1200px; overflow: hidden; background: var(--page); }
  body { position: relative; font-family: "Montserrat", sans-serif; }

  .card {
    position: absolute;
    left: 100px;
    width: 782px;
    height: 477px;
    overflow: hidden;
    box-shadow: 0 14px 40px rgba(0, 0, 0, 0.22);
  }
  .card-front { top: 79px; background: var(--front-base); }
  .card-back { top: 644px; background: var(--back-base); }

  .card-backdrop { position: absolute; inset: 0; }
  .card-front .card-backdrop {
    background: radial-gradient(ellipse 62% 95% at 55% 50%, var(--front-tone) 0%, var(--front-tone) 70%, var(--front-base) 100%);
  }
  .card-back .card-backdrop {
    background: radial-gradient(ellipse 62% 95% at 55% 50%, var(--back-base) 0%, var(--back-base) 70%, var(--back-tone) 100%);
  }

  .brand {
    position: absolute;
    display: flex;
    align-items: center;
    font-family: "Montserrat", sans-serif;
    font-weight: 600;
    white-space: nowrap;
  }
  .brand-dot { border-radius: 50%; flex: none; }

  .card-front .brand {
    top: 30px; left: 50%; transform: translateX(-50%);
    gap: 8px; color: var(--brand-blue); font-size: 22px; letter-spacing: 3px;
  }
  .card-front .brand-dot { width: 40px; height: 40px; background: var(--brand-blue); }

  .card-back .brand {
    top: 200px; left: 50%; transform: translateX(-50%);
    gap: 14px; color: var(--white); font-size: 40px; letter-spacing: 5px;
  }
  .card-back .brand-dot { width: 76px; height: 76px; background: var(--white); }

  .identity { position: absolute; left: 228px; top: 202px; }
  .person-name {
    font-weight: 700; font-size: 37px; line-height: 1; color: var(--brand-blue); letter-spacing: 0.5px;
  }
  .person-role {
    margin-top: 6px; font-weight: 400; font-size: 23px; line-height: 1; color: var(--ink); letter-spacing: 0.5px;
  }

  .contact-list { position: absolute; left: 300px; top: 389px; list-style: none; }
  .contact-item {
    display: flex; align-items: center; gap: 12px;
    height: 23px; font-size: 16px; font-weight: 600; color: var(--ink-strong);
  }
  .contact-item.phone { letter-spacing: 2.5px; font-weight: 700; }
  .contact-icon { width: 18px; height: 18px; flex: none; fill: var(--brand-blue); }
</style>
</head>
<body>

  <section class="card card-front" aria-label="Business card front">
    <div class="card-backdrop"></div>

    <div class="brand">
      <span class="brand-dot"></span>
      <span class="brand-name">VANTOREL</span>
    </div>

    <div class="identity">
      <h1 class="person-name">DARIO KESSLER</h1>
      <p class="person-role">CHIEF EXECUTIVE OFFICER</p>
    </div>

    <ul class="contact-list">
      <li class="contact-item phone">
        <svg class="contact-icon" viewBox="0 0 24 24" aria-hidden="true">
          <path d="M6.6 10.8a15.1 15.1 0 0 0 6.6 6.6l2.2-2.2c.3-.3.7-.4 1-.2 1.1.4 2.3.6 3.6.6.6 0 1 .4 1 1V20c0 .6-.4 1-1 1C10.6 21 3 13.4 3 4c0-.6.4-1 1-1h3.5c.6 0 1 .4 1 1 0 1.3.2 2.5.6 3.6.1.3 0 .7-.2 1z"/>
        </svg>
        <span>555-214-6082</span>
      </li>
      <li class="contact-item email">
        <svg class="contact-icon" viewBox="0 0 24 24" aria-hidden="true">
          <path d="M3 6h18v12H3zM4.5 7.5v.3L12 13l7.5-5.2v-.3zM4.5 9.6v6.9h15V9.6L12 14.8z" fill-rule="evenodd"/>
        </svg>
        <span>dario@vantorel.co</span>
      </li>
      <li class="contact-item web">
        <svg class="contact-icon" viewBox="0 0 24 24" aria-hidden="true">
          <path d="M12 2a10 10 0 1 0 0 20 10 10 0 0 0 0-20zm0 1.5c1.3 1.4 2.2 3.4 2.5 5.7h-5c.3-2.3 1.2-4.3 2.5-5.7zm-2.9.5c-.9 1.5-1.5 3.3-1.7 5.2H4.2A8.5 8.5 0 0 1 9.1 4zm5.8 0a8.5 8.5 0 0 1 4.9 5.2h-3.2c-.2-1.9-.8-3.7-1.7-5.2zM3.8 10.7h3.5v2.6H3.8a8.6 8.6 0 0 1 0-2.6zm5 0h6.4v2.6H8.8zm7.9 0h3.5a8.6 8.6 0 0 1 0 2.6h-3.5zM4.2 14.8h3.2c.2 1.9.8 3.7 1.7 5.2a8.5 8.5 0 0 1-4.9-5.2zm5.3 0h5c-.3 2.3-1.2 4.3-2.5 5.7-1.3-1.4-2.2-3.4-2.5-5.7zm7.1 0h3.2a8.5 8.5 0 0 1-4.9 5.2c.9-1.5 1.5-3.3 1.7-5.2z"/>
        </svg>
        <span>www.vantorel.co</span>
      </li>
    </ul>
  </section>

  <section class="card card-back" aria-label="Business card back">
    <div class="card-backdrop"></div>
    <div class="brand">
      <span class="brand-dot"></span>
      <span class="brand-name">VANTOREL</span>
    </div>
  </section>

</body>
</html>
```